Auto Insurance Flyer

Target Market(s)

english/spanish

Industry/Entity Type

Insurance Broker

Font styles to use
Serif

Colors

Designer to choose colors to be used in the design.

Requirements
Must have
• blend with my logo colors
Nice to have
• Eye catching call to action. Attention grabbers

```html
<!DOCTYPE html>
<html lang="en">
<head>
<meta charset="utf-8">
<title>Harbor Crest Insurance Services – Auto Insurance Flyer</title>
<link rel="stylesheet" href="https://fonts.googleapis.com/css2?family=Bodoni+Moda:wght@400;500;600&family=Oswald:wght@600&display=swap">
<style>
  :root {
    --page: #ffffff;
    --navy: #1b2233;
    --slate: #3a4254;
    --car-red: #b3161c;
    --wave-blue: #1c5a80;
    --panel-dark: #141516;
    --footer: #0b0b0c;
    --gold: #c69a63;
    --logo-blue: #2a6d93;
    --white: #ffffff;
    --tick: #d7a75c;
  }
  * { box-sizing: border-box; margin: 0; padding: 0; }
  html, body { width: 1200px; height: 1200px; overflow: hidden; background: var(--page); }
  .flyer {
    position: absolute; left: 62px; top: 220px;
    width: 1077px; height: 760px; overflow: hidden;
    background: var(--panel-dark);
    font-family: "Bodoni Moda", serif; color: var(--white);
  }
  .flyer__art { position: absolute; inset: 0; }
  .brand {
    position: absolute; left: 40px; top: 105px; width: 210px;
    text-align: center; color: var(--logo-blue);
    font-size: 19px; font-weight: 500; letter-spacing: 0.5px; line-height: 1.15;
  }
  .headline {
    position: absolute; left: 62px; top: 186px;
    font-family: "Oswald", sans-serif; font-weight: 600;
    font-size: 52px; letter-spacing: 0.5px; line-height: 1; white-space: nowrap;
  }
  .perks { position: absolute; left: 62px; top: 256px; list-style: none; }
  .perks li {
    display: flex; align-items: center; gap: 7px; white-space: nowrap;
    font-size: 20px; line-height: 25px; height: 25px;
  }
  .perks svg { width: 13px; height: 13px; flex: none; }
  .intro {
    position: absolute; left: 62px; top: 484px; width: 640px;
    font-size: 15.5px; line-height: 20px;
  }
  .quote-cta { position: absolute; left: 62px; top: 574px; font-size: 18px; white-space: nowrap; }
  .contact {
    position: absolute; top: 612px; height: 38px;
    background: var(--wave-blue);
    display: flex; align-items: center; gap: 8px; padding-left: 10px;
    font-size: 13px; letter-spacing: 0.3px; white-space: nowrap; flex-wrap: nowrap;
  }
  .contact--web { left: 61px; width: 268px; }
  .contact--phone { left: 367px; width: 268px; padding-left: 20px; gap: 6px; font-size: 12.5px; letter-spacing: 0.2px; }
  .contact--phone .phone-number { white-space: nowrap; flex: none; }
  .contact--phone .sep { width: 20px; flex: none; }
  .contact svg { width: 13px; height: 13px; flex: none; }
  .card-art { position: absolute; left: 783px; width: 135px; }
  .card-art--benefits { top: 478px; height: 82px; background: linear-gradient(110deg, #9b5a2e, #c98a4f 45%, #4f86a8); }
  .card-art--id { top: 578px; height: 84px; background: linear-gradient(180deg, #ffffff, #eef2f8); border: 1px solid #c9d3e2; }
  .footer {
    position: absolute; left: 0; right: 0; bottom: 0; height: 72px;
    background: var(--footer);
    display: flex; align-items: center; gap: 8px; padding-left: 62px;
    font-size: 13px; letter-spacing: 0.3px; white-space: nowrap;
  }
  .footer svg { width: 13px; height: 13px; }
</style>
</head>
<body>
<main class="flyer">
  <svg class="flyer__art" viewBox="0 0 1077 760" width="1077" height="760" aria-hidden="true">
    <defs>
      <linearGradient id="hero-tones" x1="0" y1="0" x2="1" y2="0">
        <stop offset="0" stop-color="#1c2232"/>
        <stop offset="0.42" stop-color="#3a4254"/>
        <stop offset="0.62" stop-color="#8f1a1f"/>
        <stop offset="1" stop-color="#c0171c"/>
      </linearGradient>
      <linearGradient id="lower-panel" x1="0" y1="0" x2="0" y2="1">
        <stop offset="0" stop-color="#1a1b1d"/>
        <stop offset="1" stop-color="#101112"/>
      </linearGradient>
    </defs>
    <rect x="0" y="0" width="1077" height="760" fill="url(#lower-panel)"/>
    <path d="M0 0 H1077 V228 C860 330 560 420 340 412 C200 406 80 392 0 386 Z" fill="url(#hero-tones)"/>
    <path d="M0 386 C80 392 200 406 340 412 C560 420 860 330 1077 228 V240 C860 345 560 440 340 440 C200 440 80 430 0 424 Z" fill="var(--wave-blue)"/>
  </svg>
  <div class="flyer__art" role="img" aria-label="Photo of a red SUV on a mountain road at dusk" style="height:400px"></div>

  <div class="brand">Harbor Crest<br>Insurance Services</div>

  <h1 class="headline">DUI- NO PROBLEM</h1>
  <ul class="perks">
    <li><svg viewBox="0 0 14 14"><circle cx="7" cy="7" r="6" fill="none" stroke="var(--tick)" stroke-width="1.4"/><path d="M4 7.2l2 2 4-4" fill="none" stroke="var(--tick)" stroke-width="1.4"/></svg>Foreign License-No problem</li>
    <li><svg viewBox="0 0 14 14"><circle cx="7" cy="7" r="6" fill="none" stroke="var(--tick)" stroke-width="1.4"/><path d="M4 7.2l2 2 4-4" fill="none" stroke="var(--tick)" stroke-width="1.4"/></svg>AFFORDABLE INSURANCE FOR</li>
    <li><svg viewBox="0 0 14 14"><circle cx="7" cy="7" r="6" fill="none" stroke="var(--tick)" stroke-width="1.4"/><path d="M4 7.2l2 2 4-4" fill="none" stroke="var(--tick)" stroke-width="1.4"/></svg>COLLEGE StudentS</li>
    <li><svg viewBox="0 0 14 14"><circle cx="7" cy="7" r="6" fill="none" stroke="var(--tick)" stroke-width="1.4"/><path d="M4 7.2l2 2 4-4" fill="none" stroke="var(--tick)" stroke-width="1.4"/></svg>Tickets/accidents no problem</li>
  </ul>

  <p class="intro">We can provide full coverage, liability insurance And if you are having trouble affording car insurance please ask about our california state low cost insurance policy. If you have medical card and/or food stamp card then you are already pre qualified.</p>

  <p class="quote-cta">Get quote on our website</p>

  <div class="contact contact--web">
    <svg viewBox="0 0 14 14"><circle cx="7" cy="7" r="6" fill="none" stroke="#fff" stroke-width="1.2"/><path d="M1 7h12M7 1c-3 3.5-3 8.5 0 12M7 1c3 3.5 3 8.5 0 12" fill="none" stroke="#fff" stroke-width="1"/></svg>
    www.harborcrestinsurance.com
  </div>
  <div class="contact contact--phone">
    <svg viewBox="0 0 14 14"><circle cx="7" cy="7" r="7" fill="#fff"/><path d="M5 3.5l1.3 2-0.8 0.9c0.5 1 1.2 1.7 2.1 2.1l0.9-0.8 2 1.3-0.8 1.4c-2.8-0.3-5.1-2.6-5.4-5.4z" fill="var(--wave-blue)"/></svg>
    <span class="phone-number">925-555-0142</span><span class="sep"></span>
    <svg viewBox="0 0 14 14"><circle cx="7" cy="7" r="7" fill="#fff"/><path d="M5 3.5l1.3 2-0.8 0.9c0.5 1 1.2 1.7 2.1 2.1l0.9-0.8 2 1.3-0.8 1.4c-2.8-0.3-5.1-2.6-5.4-5.4z" fill="var(--wave-blue)"/></svg>
    <span class="phone-number">(510) 555-0187</span>
  </div>

  <div class="card-art card-art--benefits" role="img" aria-label="State food benefits card with coastal scene"></div>
  <div class="card-art card-art--id" role="img" aria-label="State benefits identification card"></div>

  <footer class="footer">
    <svg viewBox="0 0 14 14"><circle cx="7" cy="7" r="7" fill="#fff"/><path d="M7 3a2.6 2.6 0 0 1 2.6 2.6C9.6 7.6 7 10.8 7 10.8S4.4 7.6 4.4 5.6A2.6 2.6 0 0 1 7 3z" fill="#0b0b0c"/><circle cx="7" cy="5.6" r="0.9" fill="#fff"/></svg>
    Oakland, Concord, pittsburg, antioch and brentwood
  </footer>
</main>
</body>
</html>
```